Web Design for Small Healthcare Startup

Hello,

We are seeking a Website Design for a healthcare company focusing on mobile vaccinations, employee health and wellness services onsite at businesses, and consulting services relating to Healthcare Entities in WA state. Our company’s mission is to “To aid in a healthier workplace”. Brightpath Rovers will provide on-site wellness services to employers that simplify and streamline employee preventative health as well as onsite consulting services to help with compliance of Healthcare Entities.

We are seeking a Website Design for Brightpath Rovers, PLLC. Our company’s mission is to provide mobile health and wellness services to employers onsite at their businesses. These services include mobile vaccinations clinics for employees as well as wellness and health screenings. The company will also offer healtcare compliance consulting services for Healthcare Entities. The company was founded to bring these important healthcare services to businesses and keep employees healthy. Healthy employees are the cornerstone to a great business and we want to help orginazations achieve their goals of having a healthy productive workforce.

We are looking for a moderin website design that will need to be coded. We have attached our current Kitework for reference as well as a brief questionare regarding our business for your information (not necessary to include all information). We would like something SEO friendly and easy to navigate.

Thank you!

Brightpath Rovers, PLLC

Target Market(s)

Small Businesses

Industry/Entity Type

Healthcare

Coding

Coded - Design and coding required

Number of Pages Required

1 page

Requirements
Nice to have
• SEO Friendly, Incorporate Logo

```html
<!DOCTYPE html>
<html lang="en">
<head>
<meta charset="utf-8">
<title>Brightpath Rovers, PLLC – Mobile Vaccine Clinics</title>
<link href="https://fonts.googleapis.com/css2?family=Jost:wght@400;500;600;700&display=swap" rel="stylesheet">
<style>
:root{
  --blue:#0b4fb3;
  --blue-deep:#0a3f96;
  --magenta:#b03ca8;
  --orange:#f26b30;
  --ink:#1b1c22;
  --text:#4a4c55;
  --muted:#8a8d96;
  --teal:#1e6a6c;
  --teal-dark:#0f4a4f;
  --soft:#eef0f3;
  --footer:#14161d;
  --white:#ffffff;
}
*{box-sizing:border-box;margin:0;padding:0}
html,body{width:1200px;height:3143px;overflow:hidden;background:var(--white)}
body{font-family:"Jost",sans-serif;color:var(--ink);position:relative}
.abs{position:absolute}
a{color:inherit;text-decoration:none}

/* header */
.brand{left:200px;top:40px;width:140px;height:80px;display:flex;align-items:center;gap:8px}
.brand-mark{width:14px;height:14px;border-radius:50%;background:var(--magenta);flex:none}
.brand-name{font-size:19px;font-weight:700;color:var(--blue);line-height:1.05}
.brand-name small{display:block;font-size:11px;font-weight:600;color:var(--blue)}
.topline{left:694px;top:56px;display:flex;align-items:center;gap:8px;font-size:13px;font-weight:500}
.topline svg{width:14px;height:14px}
.socials{display:flex;gap:8px}
.socials span{width:29px;height:29px;border-radius:50%;background:var(--blue);display:block}
.socials span.alt{background:var(--magenta)}
.header-social{left:855px;top:50px}
.nav{left:496px;top:92px;display:flex;gap:0;font-size:11px;font-weight:600;letter-spacing:.3px}
.nav a{position:absolute;white-space:nowrap}
.nav a.active{color:var(--magenta);border-bottom:2px solid var(--magenta);padding-bottom:2px}

/* hero + why */
.intro-bg{left:0;top:124px;width:1200px;height:1003px;background:linear-gradient(180deg,#f4f5f7,#eceef1)}
.hero-art{left:2px;top:124px}
.hero-title{left:200px;top:282px;width:800px;text-align:center;color:var(--white);font-size:30px;font-weight:500;line-height:37px}
.pill{display:inline-block;border-radius:20px;color:var(--white);font-weight:600;font-size:11.5px;text-align:center}
.pill.blue{background:var(--blue)}
.pill.magenta{background:var(--magenta)}
.hero-btn{left:474px;top:414px;width:253px;height:30px;line-height:30px}
.dots{display:flex;gap:10px}
.dots i{width:10px;height:10px;border-radius:50%;border:1.5px solid var(--white);display:block}
.dots i.on{background:var(--white)}
.hero-dots{left:566px;top:562px}

.why-photo{left:200px;top:696px;width:392px;height:396px;border-radius:50%;background:linear-gradient(135deg,#d9c6b4,#a58b78 55%,#6f5a4d);border:4px solid var(--magenta);border-left-color:transparent;border-top-color:#e7e2dd}
.why{left:613px;top:748px;width:420px}
.why-kicker{color:var(--blue);font-size:14px;font-weight:500}
.why-title{font-size:31px;font-weight:500;margin:4px 0 10px;line-height:1.15}
.why-list{list-style:none;font-size:12.5px;color:var(--text);line-height:15px}
.why-list li{position:relative;padding-left:22px;margin-bottom:14px}
.why-list li svg{position:absolute;left:0;top:1px;width:12px;height:12px}
.why-btn{left:613px;top:1008px;width:137px;height:29px;line-height:29px}

.bars{left:2px;top:1125px;width:1196px;height:5px}
.bars i{position:absolute;top:0;height:5px;width:290px}

/* services */
.section-title{font-size:29px;font-weight:500;text-align:center;width:1200px;left:0}
.services-title{top:1180px}
.services-lead{left:300px;top:1225px;width:600px;text-align:center;font-size:10.5px;line-height:15px;color:var(--text)}
.service{width:170px;text-align:center;font-size:12px;font-weight:600;line-height:15px}
.service .dot{width:68px;height:68px;border-radius:50%;margin:0 auto 12px;display:flex;align-items:center;justify-content:center}
.service .dot svg{width:28px;height:28px}
.services-btn{left:532px;top:1436px;width:137px;height:29px;line-height:29px}

/* reserve */
.reserve{left:2px;top:1613px;width:1196px;height:287px;background:linear-gradient(90deg,#1259b8,#0a6fd0 55%,#0b4fb3)}
.reserve-photo{left:2px;top:1613px;width:726px;height:287px;background:linear-gradient(90deg,rgba(40,90,170,.55),rgba(20,110,200,0))}
.reserve-title{left:201px;top:1688px;color:var(--white);font-size:29px;font-weight:500;line-height:37px}
.reserve-btn{left:202px;top:1786px;width:137px;height:29px;line-height:29px}

.calendar{left:728px;top:1527px;width:373px;height:443px;background:var(--white);box-shadow:0 6px 24px rgba(0,0,0,.12);padding:22px 18px}
.cal-head{display:flex;align-items:center;justify-content:space-between;font-size:13px;font-weight:600;padding:0 6px 14px;border-bottom:2px solid #dfe1e6}
.cal-month{display:flex;align-items:center;gap:26px}
.cal-month b{color:#c7c9cf;font-weight:400;font-size:15px}
.cal-toggle{display:flex;background:#eceef1;border-radius:12px;padding:2px;font-size:9px;font-weight:500}
.cal-toggle span{padding:3px 14px;border-radius:10px;color:#9a9ca4}
.cal-toggle span.on{background:var(--white);color:var(--ink)}
.cal-grid{display:grid;grid-template-columns:repeat(7,1fr);margin-top:28px;font-size:9px;text-align:center;color:#555}
.cal-grid .dow{font-weight:600;color:var(--ink);padding-bottom:26px}
.cal-grid .day{height:50px;border-top:1px solid #eceef1;display:flex;align-items:center;justify-content:center}
.cal-grid .day.out{color:#b5b7bd}
.cal-grid .day.mark span{width:22px;height:22px;border-radius:50%;border:1.5px solid var(--magenta);display:flex;align-items:center;justify-content:center;font-weight:600;color:var(--ink)}

/* clients */
.clients-title{top:2024px}
.client{top:2088px;width:149px;height:78px;background:var(--white);box-shadow:0 2px 10px rgba(0,0,0,.09);display:flex;align-items:center;justify-content:center;gap:7px;font-size:15px;font-weight:600;color:var(--ink)}
.client i{width:12px;height:12px;display:block;border-radius:50%;background:var(--ink)}
.clients-dots{left:569px;top:2198px}
.clients-dots i{border-color:var(--blue)}
.clients-dots i.on{background:var(--blue)}

/* how it works */
.how-art{left:2px;top:2262px}
.how-title{top:2384px}
.step{width:220px;text-align:center;font-size:12px;font-weight:600;line-height:16px}
.step .ring{width:72px;height:72px;border-radius:50%;border:2px solid var(--magenta);margin:0 auto 14px;display:flex;align-items:center;justify-content:center;position:relative;background:#f3f3f5}
.step .ring svg{width:28px;height:28px}
.step .num{position:absolute;top:-9px;left:50%;margin-left:-8px;width:16px;height:16px;border-radius:50%;border:1.5px solid var(--magenta);background:#f3f3f5;font-size:8.5px;line-height:13px;color:var(--magenta)}
.how-btn{left:535px;top:2611px;width:130px;height:29px;line-height:29px}

/* footer */
.footer{left:2px;top:2676px;width:1196px;height:401px;background:var(--footer);overflow:hidden}
.footer-wave{left:2px;top:2660px}
.footer-brand{left:200px;top:2806px;display:flex;align-items:center;gap:10px}
.footer-brand .brand-mark{width:16px;height:16px}
.footer-brand .brand-name{color:var(--white);font-size:21px}
.footer-brand .brand-name small{color:var(--white);font-size:12px}
.fcol{top:2800px;color:var(--white)}
.fcol h4{font-size:11px;font-weight:600;letter-spacing:.6px;margin-bottom:18px}
.fcol ul{list-style:none;font-size:9.5px;line-height:22.6px;color:#d5d7de}
.fcol li{display:flex;gap:8px;align-items:flex-start}
.fcol li svg{width:11px;height:11px;margin-top:5px;flex:none}
.fcol .addr{line-height:13px;padding:6px 0 4px}
.footer-social{left:557px;top:2957px}
.footer-social span{width:24px;height:24px}
.footer-rule{left:200px;top:3012px;width:800px;height:1px;background:#3a3d47}
.copyright{left:0;top:3037px;width:1200px;text-align:center;color:#d5d7de;font-size:9px}
.copyright em{font-style:normal;color:var(--blue)}
.copyright .sep{margin:0 12px}
.to-top{left:964px;top:3033px}
</style>
</head>
<body>

<!-- header -->
<header>
  <a class="brand abs" href="#home"><span class="brand-mark"></span><span class="brand-name">Brightpath Rovers<small>PLLC</small></span></a>
  <div class="topline abs">
    <svg viewBox="0 0 24 24" fill="none" stroke="#b03ca8" stroke-width="2"><path d="M5 3h4l2 5-2.5 1.5a11 11 0 0 0 6 6L16 13l5 2v4a2 2 0 0 1-2 2A16 16 0 0 1 3 5a2 2 0 0 1 2-2"/></svg>
    <span>+555-014-2286</span>
  </div>
  <div class="socials header-social abs"><span></span><span class="alt"></span><span></span><span></span></div>
  <nav class="nav abs">
    <a class="active" href="#home" style="left:0">HOME</a>
    <a href="#about" style="left:68px">ABOUT US</a>
    <a href="#services" style="left:154px">SERVICES</a>
    <a href="#schedule" style="left:238px">SCHEDULE TODAY</a>
    <a href="#pricing" style="left:360px">PRICING</a>
    <a href="#contact" style="left:438px">CONTACT US</a>
  </nav>
</header>

<!-- hero + why choose us -->
<div class="intro-bg abs"></div>
<svg class="hero-art abs" width="1196" height="540" viewBox="0 0 1196 540">
  <defs>
    <linearGradient id="heroFill" x1="0" y1="0" x2="1" y2="1">
      <stop offset="0" stop-color="#2b7c7d"/>
      <stop offset=".55" stop-color="#1e6a6c"/>
      <stop offset="1" stop-color="#0f4a4f"/>
    </linearGradient>
  </defs>
  <path d="M0 0H1196V170C1040 420 760 545 560 520C330 492 140 390 0 300Z" fill="url(#heroFill)" role="img" aria-label="Photo of a stethoscope resting on a desk beside notebooks"/>
  <path d="M85 325C250 450 420 515 600 520C840 526 1040 420 1196 240" fill="none" stroke="#0b4fb3" stroke-width="9" stroke-linecap="round"/>
</svg>
<h1 class="hero-title abs">Brightpath Rovers is a mobile vaccine clinic providing employers on-site, seamless, hassle-free vaccine clinics for their employees.</h1>
<a class="pill blue hero-btn abs" href="#about">Making the workplace a healthier place</a>
<div class="dots hero-dots abs"><i></i><i class="on"></i><i></i><i></i></div>

<div class="why-photo abs" role="img" aria-label="Photo of a caregiver talking with a smiling senior woman in a wheelchair"></div>
<section class="why abs" id="about">
  <p class="why-kicker">Why choose us</p>
  <h2 class="why-title">Brightpath Rovers, PLLC</h2>
  <ul class="why-list">
    <li><svg viewBox="0 0 24 24" fill="none" stroke="#b03ca8" stroke-width="2"><path d="M8 3l-5 5 13 13 5-5zM14 3l7 7"/></svg>Brightpath Rovers specializes in providing seamless, hassle-free, on-site mobile vaccine clinics.</li>
    <li><svg viewBox="0 0 24 24" fill="none" stroke="#b03ca8" stroke-width="2"><path d="M8 3l-5 5 13 13 5-5zM14 3l7 7"/></svg>No crowded waiting rooms, no long lines, no hassle!</li>
    <li><svg viewBox="0 0 24 24" fill="none" stroke="#b03ca8" stroke-width="2"><path d="M8 3l-5 5 13 13 5-5zM14 3l7 7"/></svg>Specializing in workplace employee vaccine clinics. Great service to offer as part of your company's Employee Wellness Package.</li>
    <li><svg viewBox="0 0 24 24" fill="none" stroke="#b03ca8" stroke-width="2"><path d="M8 3l-5 5 13 13 5-5zM14 3l7 7"/></svg>Offering Flu and Covid vaccinations</li>
  </ul>
</section>
<a class="pill blue why-btn abs" href="#schedule">Schedule today</a>

<div class="bars abs">
  <i style="left:0;background:var(--blue)"></i>
  <i style="left:301px;background:var(--magenta)"></i>
  <i style="left:603px;background:var(--orange)"></i>
  <i style="left:906px;background:var(--ink)"></i>
</div>

<!-- services -->
<h2 class="section-title services-title abs" id="services">Our Services</h2>
<p class="services-lead abs">It is a long established fact that a reader will be distracted by the readable content of a page when looking at its layout. The point of using Lorem Ipsum is that it has a more-or-less normal distribution</p>

<div class="service abs" style="left:103px;top:1282px">
  <div class="dot" style="background:var(--blue)"><svg viewBox="0 0 24 24" fill="none" stroke="#fff" stroke-width="1.8"><rect x="7" y="2.5" width="10" height="19" rx="2"/><path d="M11 18h2"/></svg></div>
  Mobile vaccine clinics providing Flu,
</div>
<div class="service abs" style="left:309px;top:1282px">
  <div class="dot" style="background:var(--magenta)"><svg viewBox="0 0 24 24" fill="none" stroke="#fff" stroke-width="1.8"><path d="M12 2.5l8 3v6c0 5-3.5 8.5-8 10-4.5-1.5-8-5-8-10v-6z"/></svg></div>
  Covid booster,
</div>
<div class="service abs" style="left:515px;top:1282px">
  <div class="dot" style="background:var(--blue)"><svg viewBox="0 0 24 24" fill="none" stroke="#fff" stroke-width="1.8"><path d="M16 3l5 5L9 20H4v-5zM13 6l5 5"/></svg></div>
  Pneumonia vaccines,
</div>
<div class="service abs" style="left:720px;top:1282px">
  <div class="dot" style="background:var(--magenta)"><svg viewBox="0 0 24 24" fill="none" stroke="#fff" stroke-width="1.8"><path d="M12 20S3 14.5 3 8.5A4.5 4.5 0 0 1 12 6a4.5 4.5 0 0 1 9 2.5C21 14.5 12 20 12 20z"/><path d="M6 12h3l2-3 2 5 2-2h3"/></svg></div>
  Wellness screenings, and
</div>
<div class="service abs" style="left:925px;top:1282px">
  <div class="dot" style="background:var(--blue)"><svg viewBox="0 0 24 24" fill="none" stroke="#fff" stroke-width="1.8"><path d="M4 15v-3a8 8 0 0 1 16 0v3"/><rect x="3" y="14" width="4" height="6" rx="1.5"/><rect x="17" y="14" width="4" height="6" rx="1.5"/></svg></div>
  Consulting services for WA healthcare entities
</div>
<a class="pill magenta services-btn abs" href="#schedule">Schedule today</a>

<!-- reserve -->
<section id="schedule">
  <div class="reserve abs"></div>
  <div class="reserve-photo abs" role="img" aria-label="Faded photo of a professional working at a laptop"></div>
  <h2 class="reserve-title abs">Reserve your on-site<br>mobile vaccine clinic today!</h2>
  <a class="pill magenta reserve-btn abs" href="#contact">Contact us today!</a>

  <div class="calendar abs">
    <div class="cal-head">
      <div class="cal-month"><b>‹</b><span>July 2022</span><b>›</b></div>
      <div class="cal-toggle"><span class="on">Month</span><span>Year</span></div>
    </div>
    <div class="cal-grid">
      <div class="dow">Mon</div><div class="dow">Tue</div><div class="dow">Wed</div><div class="dow">Thu</div><div class="dow">Fri</div><div class="dow">Sat</div><div class="dow">Sun</div>
      <div class="day out">27</div><div class="day out">28</div><div class="day out">29</div><div class="day out">30</div><div class="day">1</div><div class="day">2</div><div class="day">3</div>
      <div class="day">4</div><div class="day">5</div><div class="day">6</div><div class="day">7</div><div class="day">8</div><div class="day">9</div><div class="day">10</div>
      <div class="day">11</div><div class="day">12</div><div class="day">13</div><div class="day">14</div><div class="day">15</div><div class="day">16</div><div class="day">17</div>
      <div class="day">18</div><div class="day">19</div><div class="day mark"><span>20</span></div><div class="day">21</div><div class="day mark"><span>22</span></div><div class="day">23</div><div class="day mark"><span>24</span></div>
      <div class="day">25</div><div class="day mark"><span>26</span></div><div class="day">27</div><div class="day mark"><span>28</span></div><div class="day">29</div><div class="day">30</div><div class="day">31</div>
    </div>
  </div>
</section>

<!-- clients -->
<h2 class="section-title clients-title abs">Our clients</h2>
<div class="client abs" style="left:200px"><i></i>Northgate</div>
<div class="client abs" style="left:362px"><i></i>Fernleaf</div>
<div class="client abs" style="left:524px"><i></i>Solvane</div>
<div class="client abs" style="left:686px"><i></i>Kitework</div>
<div class="client abs" style="left:848px"><i></i>Meridel</div>
<div class="dots clients-dots abs"><i></i><i class="on"></i><i></i><i></i></div>

<!-- how it works -->
<svg class="how-art abs" width="1196" height="460" viewBox="0 0 1196 460">
  <path d="M0 250C260 20 460 8 598 8S936 20 1196 250V460H0Z" fill="#f1f2f4"/>
  <path d="M140 220C330 50 470 10 598 10S866 50 1056 220" fill="none" stroke="#0b4fb3" stroke-width="9" stroke-linecap="round"/>
</svg>
<h2 class="section-title how-title abs">How it works</h2>
<div class="step abs" style="left:216px;top:2446px">
  <div class="ring"><span class="num">1</span><svg viewBox="0 0 24 24" fill="none" stroke="#0b4fb3" stroke-width="1.8"><path d="M6 2.5h8l4 4v15H6z"/><path d="M9 11h6M9 14h6M9 17h6"/></svg></div>
  Submit Vaccine Clinic Needs Questionnaire.
</div>
<div class="step abs" style="left:490px;top:2446px">
  <div class="ring"><span class="num">2</span><svg viewBox="0 0 24 24" fill="none" stroke="#0b4fb3" stroke-width="1.8"><path d="M5 3h4l2 5-2.5 1.5a11 11 0 0 0 6 6L16 13l5 2v4a2 2 0 0 1-2 2A16 16 0 0 1 3 5a2 2 0 0 1 2-2"/><path d="M14 3a7 7 0 0 1 7 7M14 7a3 3 0 0 1 3 3"/></svg></div>
  Brightpath Rovers, PLLC will contact you to schedule on-site vaccine clinic.
</div>
<div class="step abs" style="left:763px;top:2446px">
  <div class="ring"><span class="num">3</span><svg viewBox="0 0 24 24" fill="none" stroke="#0b4fb3" stroke-width="1.8"><rect x="3" y="5" width="18" height="16" rx="1.5"/><path d="M3 10h18M8 3v4M16 3v4M7 13h2M11 13h2M15 13h2M7 17h2M11 17h2M15 17h2"/></svg></div>
  Prepare your employees for vaccine clinic day.
</div>
<a class="pill magenta how-btn abs" href="#schedule">Schedule today</a>

<!-- footer -->
<footer id="contact">
  <div class="footer abs"></div>
  <svg class="footer-wave abs" width="1196" height="70" viewBox="0 0 1196 70">
    <path d="M0 30C200 -5 420 20 598 52C780 82 1000 20 1196 32V70H0Z" fill="#14161d"/>
    <path d="M0 28C200 -8 420 16 598 48C780 78 1000 16 1196 30" fill="none" stroke="#0b4fb3" stroke-width="10"/>
  </svg>
  <div class="footer-brand abs"><span class="brand-mark"></span><span class="brand-name">Brightpath Rovers<small>PLLC</small></span></div>

  <div class="fcol abs" style="left:407px">
    <h4>QUICK LINKS</h4>
    <ul><li>Home</li><li>About Us</li><li>Services</li><li>Schedule Today</li><li>Pricing</li><li>Contact Us</li></ul>
  </div>
  <div class="fcol abs" style="left:545px">
    <h4>CONTACT US</h4>
    <ul>
      <li><svg viewBox="0 0 24 24" fill="none" stroke="#b03ca8" stroke-width="2"><path d="M5 3h4l2 5-2.5 1.5a11 11 0 0 0 6 6L16 13l5 2v4a2 2 0 0 1-2 2A16 16 0 0 1 3 5a2 2 0 0 1 2-2"/></svg>555-014-2286</li>
      <li><svg viewBox="0 0 24 24" fill="none" stroke="#b03ca8" stroke-width="2"><rect x="3" y="5" width="18" height="14" rx="1.5"/><path d="M3 6l9 7 9-7"/></svg>hello@brightpathrovers.com</li>
      <li class="addr"><svg viewBox="0 0 24 24" fill="none" stroke="#b03ca8" stroke-width="2" style="margin-top:1px"><path d="M12 21s7-6.5 7-12a7 7 0 0 0-14 0c0 5.5 7 12 7 12z"/><circle cx="12" cy="9" r="2.5"/></svg><span>18 Harbor Lane, Tacoma,<br>WA 98402</span></li>
    </ul>
  </div>
  <div class="socials footer-social abs"><span></span><span class="alt"></span><span></span><span></span></div>
  <div class="fcol abs" style="left:762px">
    <h4>OUR SERVICES</h4>
    <ul><li>Mobile vaccine clinics providing Flu,</li><li>Covid booster,</li><li>Pneumonia vaccines,</li><li>Wellness screenings, and</li><li>Consulting services for WA Healthcare Entities</li></ul>
  </div>

  <div class="footer-rule abs"></div>
  <p class="copyright abs">© 2022 <em>Brightpath Rovers</em> All Right Reserved<span class="sep">|</span>Terms and Conditions<span class="sep">|</span>Privacy Policy</p>
  <svg class="to-top abs" width="14" height="16" viewBox="0 0 14 16"><path d="M7 0L14 16L7 12L0 16Z" fill="#b03ca8"/></svg>
</footer>

</body>
</html>
```